Re-design association of teachers webplattform

I need a complete re-design for an existing association of teachers website. I will create it in wordpress in the next months.

It should be modern, but more an information plattform for teachers in our region (Switzerland, south -> near the alps).
Following content are contained:
- blog
- calendar
- text only
- document only (a list of documents to download -> pdf)
- social media
- login area

What I need is :
- a well color concept
- an inspiration how to use images (or without images)
- an inspiration where to place logo (attached file) / text / navigation

```html
<!DOCTYPE html>
<html lang="en">
<head>
<meta charset="utf-8">
<title>Alpora – Association of Teachers</title>
<link href="https://fonts.googleapis.com/css2?family=Open+Sans:wght@400;600;700&display=swap" rel="stylesheet">
<style>
:root{
  --blue:#0aa0d9;
  --blue-soft:#e3f3fb;
  --ink:#2c3548;
  --text:#3d4556;
  --muted:#8b93a3;
  --light:#f4f6f9;
  --dark:#1e2638;
  --dark-line:#343d52;
  --white:#fff;
}
*{box-sizing:border-box;margin:0;padding:0}
html,body{width:1200px;height:3743px;overflow:hidden}
body{font-family:"Open Sans",Arial,sans-serif;color:var(--text);background:var(--white);position:relative}
.wrap{position:absolute;inset:0}
section,header,footer{position:absolute;left:0;width:1200px}
.abs{position:absolute}

/* header */
.site-header{top:0;height:80px;background:var(--blue)}
.brand{left:155px;top:12px;width:102px;height:73px;background:var(--white);display:flex;align-items:center;justify-content:center;gap:6px;font-weight:700;font-size:20px;color:var(--blue);z-index:2}
.brand i{width:10px;height:10px;border-radius:50%;background:var(--blue);display:block}
.nav{left:360px;top:43px;display:flex;gap:0;font-size:13px;font-weight:600;color:var(--white)}
.nav a{position:absolute;white-space:nowrap;color:var(--white);text-decoration:none}
.login-btn{left:931px;top:35px;width:114px;height:35px;background:var(--blue-soft);color:var(--blue);font-size:12px;display:flex;align-items:center;justify-content:center;border-radius:2px}
.util{left:975px;top:6px;display:flex;gap:18px;align-items:center;color:var(--white);font-size:12px;font-weight:700}

/* hero */
.hero{top:80px;height:532px;background:linear-gradient(100deg,#5a4b45 0%,#8a7468 35%,#c9b5a3 60%,#e8dccd 78%,#6e5a4c 100%)}
.hero::after{content:"";position:absolute;inset:0;background:linear-gradient(90deg,rgba(20,20,30,.45),rgba(20,20,30,0) 60%)}
.hero-copy{position:absolute;left:155px;top:150px;z-index:1;color:var(--white)}
.hero h1{font-size:52px;font-weight:400;line-height:58px;letter-spacing:.3px}
.hero p{margin-top:16px;font-size:15px;font-weight:600;line-height:25px;width:490px}
.hero .btn{margin-top:26px;width:139px;height:41px;background:var(--white);color:var(--blue);font-size:12px;display:flex;align-items:center;justify-content:center;border-radius:2px}

/* intro */
.intro{top:612px;height:500px}
.intro h2{position:absolute;left:155px;top:80px;width:500px;font-size:41px;font-weight:400;line-height:50px;color:var(--ink)}
.intro .lead{position:absolute;left:155px;top:250px;width:440px;font-size:13.5px;font-weight:600;line-height:22px;color:var(--ink)}
.intro .body{position:absolute;left:155px;top:305px;width:450px;font-size:12px;line-height:22.5px;color:var(--muted)}
.calendar{position:absolute;left:686px;top:74px;width:356px;height:356px;background:var(--white);box-shadow:0 6px 24px rgba(30,40,60,.12)}
.cal-head{height:55px;background:var(--blue);display:flex;align-items:center;justify-content:space-between;padding:0 18px;color:var(--white);font-weight:600;font-size:17px}
.cal-month{width:62px;height:26px;background:var(--white);border-radius:2px;color:var(--ink);font-size:12px;font-weight:400;display:flex;align-items:center;justify-content:space-between;padding:0 10px}
.cal-grid{display:grid;grid-template-columns:repeat(7,1fr);padding:10px 10px 0;row-gap:0}
.cal-grid span{height:48px;display:flex;align-items:center;justify-content:center;font-size:14px;color:var(--ink)}
.cal-grid .dow{height:28px;font-size:13px;color:var(--muted)}
.cal-grid .out{color:#b7bcc7}
.cal-grid .today b{width:36px;height:36px;border-radius:50%;background:var(--blue);color:var(--white);display:flex;align-items:center;justify-content:center;font-weight:600}

/* articles */
.articles{top:1112px;height:611px;background:var(--light)}
.sec-title{position:absolute;left:0;width:1200px;text-align:center;font-size:41px;font-weight:400;line-height:50px;color:var(--ink)}
.articles .sec-title{top:82px}
.card{position:absolute;width:277px}
.photo{background:linear-gradient(135deg,#7c8a94,#c8ccd0)}
.date{font-size:10px;font-weight:700;letter-spacing:1.5px;color:var(--blue)}
.card h3{font-size:19px;font-weight:400;line-height:26px;color:var(--ink);margin-top:8px}
.card p{font-size:12px;line-height:22.5px;color:var(--muted);margin-top:14px}
.card p a{color:var(--blue);text-decoration:none}
.arrow{position:absolute;top:1403px;color:var(--ink)}

/* documents */
.docs{top:1723px;height:900px}
.docs .sec-title{top:73px}
.doc{position:absolute;width:275px}
.doc h3{font-size:19px;font-weight:400;line-height:26px;color:var(--ink)}
.doc p{font-size:12px;line-height:22.5px;color:var(--muted);margin-top:14px}
.pdf-btn{position:absolute;width:203px;height:44px;background:var(--blue-soft);color:var(--blue);font-size:10px;font-weight:700;letter-spacing:1.5px;display:flex;align-items:center;justify-content:center;gap:12px}
.pdf-btn.active{background:var(--blue);color:var(--white);box-shadow:0 6px 16px rgba(10,160,217,.35)}

/* social */
.social{top:2623px;height:623px;background:var(--light)}
.social .sec-title{top:80px}
.feed-panel{position:absolute;left:155px;top:175px;width:89px;height:352px;background:var(--blue);display:flex;flex-direction:column;align-items:center;justify-content:space-between;padding:26px 0}
.feed-panel .dot{width:34px;height:34px;border-radius:50%;background:var(--white)}
.post{position:absolute;top:2819px;width:234px}
.post-head{display:flex;gap:10px;align-items:center}
.avatar{width:46px;height:46px;border-radius:50%;background:linear-gradient(135deg,#8e7a6b,#d6c4b3)}
.post-head b{display:block;font-size:13px;font-weight:600;color:var(--ink)}
.post-head small{font-size:10px;color:var(--muted)}
.post p{margin-top:12px;font-size:10.5px;line-height:16px;color:var(--ink)}
.post p span{color:var(--blue)}
.post .photo{margin-top:16px;height:180px;background:linear-gradient(135deg,#3f4a55,#9aa3ab)}
.stats{margin-top:20px;display:flex;gap:14px;align-items:center;font-size:10px;color:var(--ink)}
.stats span{display:flex;align-items:center;gap:6px}

/* cta + footer */
.site-footer{top:3246px;height:497px;background:var(--dark);color:var(--white)}
.cta h2{position:absolute;left:219px;top:50px;font-size:40px;font-weight:400}
.cta p{position:absolute;left:220px;top:110px;font-size:14px;font-weight:600}
.cta .btn{position:absolute;left:798px;top:64px;width:170px;height:47px;background:var(--blue);font-size:13px;font-weight:600;display:flex;align-items:center;justify-content:center}
.rule{position:absolute;left:155px;top:215px;width:887px;height:1px;background:var(--dark-line)}
.fcol{position:absolute;top:242px;font-size:12px;color:#98a0b0}
.fcol h4{font-size:12px;font-weight:700;color:var(--white);margin-bottom:28px}
.fcol li{list-style:none;line-height:27px}
.fcol .ic{display:flex;align-items:center;gap:14px;margin-top:10px}
.fcol .ic i{width:26px;height:26px;border-radius:50%;background:var(--dark-line);display:inline-block}
.legal{position:absolute;left:155px;top:460px;font-size:10px;color:var(--white)}
.legal span{color:var(--blue)}
.socials{position:absolute;left:905px;top:452px;display:flex;gap:11px}
.socials i{width:26px;height:26px;border-radius:50%;background:var(--dark-line);display:block}
</style>
</head>
<body>
<div class="wrap">

<header class="site-header">
  <div class="abs brand">Alpora <i></i></div>
  <nav class="abs nav">
    <a style="left:0">General information</a>
    <a style="left:150px">Statutes and Protocols</a>
    <a style="left:311px">Board</a>
    <a style="left:378px">Delegates</a>
    <a style="left:467px">New members</a>
  </nav>
  <div class="abs util">
    <svg width="20" height="20" viewBox="0 0 20 20" fill="none" stroke="#fff" stroke-width="1.8"><circle cx="8.5" cy="8.5" r="6.5"/><path d="M13.5 13.5 18 18"/></svg>
    <span>EN ▾</span>
  </div>
  <div class="abs login-btn">Log in</div>
</header>

<section class="hero" role="img" aria-label="Smiling teacher holding a purple folder in a bright classroom">
  <div class="hero-copy">
    <h1>Welcome to the<br>association of teachers</h1>
    <p>Nullam blandit ut orci vel malesuada. Duis et sem quis est tincidunt aliquet non vitae metus. Morbi iaculis nulla a sodales egestas.</p>
    <div class="btn">Register now</div>
  </div>
</section>

<section class="intro">
  <h2>Proin vel diam vitae turp aliquam consequat et a est congue purus</h2>
  <p class="lead">Nullam blandit ut orci vel malesuada. Duis et sem quis est tincidunt aliquet non vitae metus. Morbi iaculis nulla a sodales egestas.</p>
  <p class="body">Proin vel diam vitae turpis aliquam consequat et a est. Vivamus congue purus a sapien laoreet aliquet. Mauris blandit lacus a arcu pulvinar tincidunt. Aliquam in felis euismod, vulputate augue in, lobortis nisl. Maecenas imperdiet elit sed sem placerat lobortis. Fusce congue velit at tellus eleifend, sit amet sodales mi elementum. Suspendisse nunc lacus, eleifend in accumsan.</p>
  <div class="calendar">
    <div class="cal-head">Calendar <div class="cal-month">Apr <svg width="10" height="6" viewBox="0 0 10 6" fill="none" stroke="#2c3548" stroke-width="1.4"><path d="M1 1l4 4 4-4"/></svg></div></div>
    <div class="cal-grid">
      <span class="dow">SUN</span><span class="dow">MON</span><span class="dow">TUE</span><span class="dow">WED</span><span class="dow">THU</span><span class="dow">FRI</span><span class="dow">SAT</span>
      <span class="out">30</span><span>1</span><span>2</span><span>3</span><span>4</span><span>5</span><span>6</span>
      <span>7</span><span>8</span><span>9</span><span>10</span><span class="today"><b>11</b></span><span>12</span><span>13</span>
      <span>14</span><span>15</span><span>16</span><span>17</span><span>18</span><span>19</span><span>20</span>
      <span>21</span><span>22</span><span>23</span><span>24</span><span>25</span><span>26</span><span>27</span>
      <span>28</span><span>29</span><span>30</span><span class="out">1</span><span class="out">2</span><span class="out">3</span><span class="out">4</span>
    </div>
  </div>
</section>

<section class="articles">
  <h2 class="sec-title">Latest articles</h2>
  <div class="card" style="left:157px;top:167px">
    <div class="photo" style="height:251px;background:linear-gradient(135deg,#2f4a3c,#d9cfc4 60%,#f1ede8)" role="img" aria-label="Teacher in a blue shirt seated at a desk by a chalkboard"></div>
    <div class="date" style="margin-top:27px">29 SEPTEMBER, 2020</div>
    <h3>Vivamus congue purus a sapien laoreet aliquet aget...</h3>
  </div>
  <div class="card" style="left:460px;top:173px">
    <div class="date">29 SEPTEMBER, 2020</div>
    <h3>Morbi vitae aliquam ante. Aenean convallis lacus eget cursus feugiat</h3>
    <p>Proin vel diam vitae turpis aliquam consequat et a est. Vivamus congue purus a sapien laoreet aliquet. Mauris blandit lacus a arcu pulvinar tincidunt. Aliquam in felis euismod, vulputate augue in, lobortis nisl. Maecenas imperdiet elit sed sem placerat lobortis. Fusce congue velit at tellus eleifend, sit amet sodales mi elementum. Suspendisse nunc lacus, eleifend in accumsan. Donec quis purus nulla. Duis eu erat sagittis, scelerisque lacus... <a>Read more</a></p>
  </div>
  <div class="card" style="left:764px;top:167px">
    <div class="photo" style="height:251px;background:linear-gradient(135deg,#dcdfe2,#8e9296 60%,#4a4e54)" role="img" aria-label="Three teachers talking in a bright meeting room"></div>
    <div class="date" style="margin-top:27px">29 SEPTEMBER, 2020</div>
    <h3>Maximus in vitae mauris. maecenas volutpat puru...</h3>
  </div>
  <svg class="arrow" style="left:119px;top:291px" width="12" height="14" viewBox="0 0 12 14" fill="none" stroke="#2c3548" stroke-width="2"><path d="M9 1 3 7l6 6"/></svg>
  <svg class="arrow" style="left:1067px;top:291px" width="12" height="14" viewBox="0 0 12 14" fill="none" stroke="#2c3548" stroke-width="2"><path d="M3 1l6 6-6 6"/></svg>
</section>

<section class="docs">
  <h2 class="sec-title">Donec maximus bibendum neque<br>et facilisis mauris ut</h2>

  <div class="doc" style="left:157px;top:215px"><h3>Dictam vitae aliquam ante. Aenean convallis lacus eget cursus feugiat</h3><p>Proin vel diam vitae turpis aliquam consequat et a est. Vivamus congue purus a sapien laoreet aliquet. Mauris blandit lacus a arcu pulvinar tincidunt. Aliquam in felis euismod, vulputate augue in, lobortis nisl.</p></div>
  <div class="doc" style="left:460px;top:215px"><h3>Vitae aliquam ante. Aenean convallis lacus eget cursus.</h3><p>Proin vel diam vitae turpis aliquam consequat et a est. Vivamus congue purus a sapien laoreet aliquet. Mauris blandit lacus a arcu pulvinar tincidunt. Aliquam in felis euismod, vulputate augue in, lobortis nisl.</p></div>
  <div class="doc" style="left:764px;top:215px"><h3>Nulla vitae aliquam ante. Aenean convallis lacus eget cursus feugiat</h3><p>Proin vel diam vitae turpis aliquam consequat et a est. Vivamus congue purus a sapien laoreet aliquet. Mauris blandit lacus a arcu pulvinar tincidunt. Aliquam in felis euismod, vulputate augue in, lobortis nisl.</p></div>

  <div class="pdf-btn" style="left:157px;top:445px"><svg width="18" height="18" viewBox="0 0 18 18" fill="none" stroke="currentColor" stroke-width="1.6"><path d="M9 2v10M5 8l4 4 4-4M2 13v3h14v-3"/></svg>DOWNLOAD PDF</div>
  <div class="pdf-btn" style="left:460px;top:422px"><svg width="18" height="18" viewBox="0 0 18 18" fill="none" stroke="currentColor" stroke-width="1.6"><path d="M9 2v10M5 8l4 4 4-4M2 13v3h14v-3"/></svg>DOWNLOAD PDF</div>
  <div class="pdf-btn active" style="left:764px;top:445px"><svg width="18" height="18" viewBox="0 0 18 18" fill="none" stroke="currentColor" stroke-width="1.6"><path d="M9 2v10M5 8l4 4 4-4M2 13v3h14v-3"/></svg>DOWNLOAD PDF</div>

  <div class="doc" style="left:157px;top:535px"><h3>Morbi vitae aliquam ante. Aenean convallis lacus eget cursus feugiat</h3><p>Proin vel diam vitae turpis aliquam consequat et a est. Vivamus congue purus a sapien laoreet aliquet. Mauris blandit lacus a arcu pulvinar tincidunt. Aliquam in felis euismod, vulputate augue in, lobortis nisl.</p></div>
  <div class="doc" style="left:460px;top:535px"><h3>Porin aliquam ante. Aenean convallis lacus eget cursus feugiat sed...</h3><p>Proin vel diam vitae turpis aliquam consequat et a est. Vivamus congue purus a sapien laoreet aliquet. Mauris blandit lacus a arcu pulvinar tincidunt. Aliquam in felis euismod, vulputate augue in, lobortis nisl.</p></div>
  <div class="doc" style="left:764px;top:535px"><h3>Ammet vitae aliquam ante. Aenean convallis lacus eget cursus feugiat</h3><p>Proin vel diam vitae turpis aliquam consequat et a est. Vivamus congue purus a sapien laoreet aliquet. Mauris blandit lacus a arcu pulvinar tincidunt. Aliquam in felis euismod, vulputate augue in, lobortis nisl.</p></div>

  <div class="pdf-btn" style="left:157px;top:764px"><svg width="18" height="18" viewBox="0 0 18 18" fill="none" stroke="currentColor" stroke-width="1.6"><path d="M9 2v10M5 8l4 4 4-4M2 13v3h14v-3"/></svg>DOWNLOAD PDF</div>
  <div class="pdf-btn" style="left:460px;top:764px"><svg width="18" height="18" viewBox="0 0 18 18" fill="none" stroke="currentColor" stroke-width="1.6"><path d="M9 2v10M5 8l4 4 4-4M2 13v3h14v-3"/></svg>DOWNLOAD PDF</div>
  <div class="pdf-btn" style="left:764px;top:764px"><svg width="18" height="18" viewBox="0 0 18 18" fill="none" stroke="currentColor" stroke-width="1.6"><path d="M9 2v10M5 8l4 4 4-4M2 13v3h14v-3"/></svg>DOWNLOAD PDF</div>
</section>

<section class="social">
  <h2 class="sec-title">Social media feed</h2>
  <div class="feed-panel">
    <svg width="20" height="12" viewBox="0 0 20 12" fill="none" stroke="#fff" stroke-width="2"><path d="M2 10l8-8 8 8"/></svg>
    <i class="dot"></i>
    <svg width="20" height="12" viewBox="0 0 20 12" fill="none" stroke="#fff" stroke-width="2"><path d="M2 2l8 8 8-8"/></svg>
  </div>
</section>

<div class="post" style="left:276px">
  <div class="post-head"><div class="avatar"></div><div><b>Education Department</b><small>@EducationOffice &nbsp;•&nbsp; 4 hr</small></div></div>
  <p><span>#ECH2022</span> libero tempore, cum soluta nobis est eligendi optio cumque nihil impedit quo minus id quod maxime placeat facere possi-mus, omnis vol...</p>
  <div class="photo" role="img" aria-label="Group of adults seated in a workshop"></div>
  <div class="stats"><span>◯ 782</span><span>⇄ 37</span><span>♡ 929</span><span>⋯</span></div>
</div>
<div class="post" style="left:543px">
  <div class="post-head"><div class="avatar"></div><div><b>Education Department</b><small>@EducationOffice &nbsp;•&nbsp; 4 hr</small></div></div>
  <p><span>#ECH2022</span> libero tempore, cum soluta nobis est eligendi optio cumque nihil impedit quo minus id quod maxime placeat facere possi-mus, omnis vol...</p>
  <div class="photo" role="img" aria-label="Colleagues gathered around a laptop in a loft office" style="background:linear-gradient(135deg,#b9aa9a,#6a6058)"></div>
  <div class="stats"><span>◯ 782</span><span>⇄ 37</span><span>♡ 929</span><span>⋯</span></div>
</div>
<div class="post" style="left:809px">
  <div class="post-head"><div class="avatar"></div><div><b>Education Department</b><small>@EducationOffice &nbsp;•&nbsp; 4 hr</small></div></div>
  <p><span>#ECH2022</span> libero tempore, cum soluta nobis est eligendi optio cumque nihil impedit quo minus id quod maxime placeat facere possi-mus, omnis vol...</p>
  <div class="photo" role="img" aria-label="Presentation in a meeting room with a screen" style="background:linear-gradient(135deg,#c9cfd6,#5b6470)"></div>
  <div class="stats"><span>◯ 782</span><span>⇄ 37</span><span>♡ 929</span><span>⋯</span></div>
</div>

<footer class="site-footer">
  <div class="cta">
    <h2>Ready to get started</h2>
    <p>Cras vulputate odio eu egestas mattis, augue lectus amet mattis odio</p>
    <div class="btn">Login now</div>
  </div>
  <div class="rule"></div>
  <div class="fcol" style="left:157px">
    <h4>Contact us</h4>
    <ul><li style="line-height:22px">12 Via Lago,<br>6900 Lugano, Ticino</li></ul>
    <div class="ic" style="margin-top:18px"><i></i>hello@alpora-teachers.ch</div>
    <div class="ic"><i></i>091-555-0142</div>
  </div>
  <div class="fcol" style="left:462px"><h4>About</h4><ul><li>Home</li><li>Browse</li><li>About</li><li>Newslette</li></ul></div>
  <div class="fcol" style="left:690px"><h4>Services</h4><ul><li>Add a topic</li><li>Contact</li><li>Blog</li></ul></div>
  <div class="fcol" style="left:918px"><h4>Support</h4><ul><li>Terms and conditions</li><li>Privacy policy</li><li>Help</li><li>Contact us</li></ul></div>
  <div class="legal">© 2022 <span>Alpora</span> . All rights reserved</div>
  <div class="socials"><i></i><i></i><i></i><i></i></div>
</footer>

</div>
</body>
</html>
```